Sensual cosmetic range, design logo and box

This is a new sub brand under the Velarisse Range of cosmetics. Velarisse is a "Glow from the Core" range of approx 30 existing products.

This new range will consist of four products initially. I am seeking an innovative look and feel for this new sub brand of sensual cosmetics products. I have uploaded two pdfs of the box for the designs to be done on . I would like the designer to design the look and feel, colours etc and name of the range (all we have is the word sensual so the designer can use that name or it can be a entirely new name as long as it portrays the word sensual in it"

This particular product is sensual massage cream. I have supplied the box dimension on the pdf( one square and one rectangular.)

Target Market(s)

female only, between the ages of 24 to 49

Industry/Entity Type

Cosmetics

Requirements
Must have
• A name and design for the new range plus colours. Currently all we have is the name "sensuals". I am not stuck on this name and we are happy to see a new name. As long as the name, design and colour portrays " sensual or sensuality "

I have also supplied the existing Velarisse logo. I will leave it up to the designer interpretation if they want the existing velarisse logo to dominate or it can be made small and not prominent at all. it can even be made black and white .

the right colour combination. The containers I am using and packaging is all white, silver and clear. the box should go with these colours and also have a senual look and feel

keep in mind it is a women's range only

```html
<!DOCTYPE html>
<html lang="en">
<head>
<meta charset="utf-8">
<title>Velarisse Sensual Massage Cream – Label and Carton</title>
<link rel="stylesheet" href="https://fonts.googleapis.com/css2?family=Pinyon+Script&display=swap">
<style>
  :root {
    --paper: #ffffff;
    --rose: #f28db2;
    --rose-line: #f4a9c5;
    --silver: #e4e4e4;
    --silver-text: #9a9a9a;
    --ink: #1e1b1c;
  }
  html, body {
    margin: 0;
    width: 1200px;
    height: 1200px;
    overflow: hidden;
    background: var(--paper);
  }
  .artboard { display: block; width: 1200px; height: 1200px; }
  .script { font-family: "Pinyon Script", cursive; }
  .dieline { fill: none; stroke: var(--rose-line); stroke-width: 0.9; }
  .crease { stroke: var(--rose-line); stroke-width: 0.6; }
  .damask-band { fill: var(--silver); }
  .rose-wave { fill: var(--rose); }
  .mark-dot { fill: var(--ink); }
  .brand-name { fill: var(--silver-text); }
  .tagline { fill: var(--silver-text); }
  .word-sensual { fill: var(--silver-text); }
  .word-massage { fill: var(--rose); }
  .word-cream { fill: var(--ink); }
</style>
</head>
<body>
<svg class="artboard" viewBox="0 0 950 950" xmlns="http://www.w3.org/2000/svg">
  <defs>
    <!-- front label used on the jar band and each side panel -->
    <g id="product-face">
      <rect class="damask-band" x="0" y="5" width="190" height="38" role="img" aria-label="Soft silver damask ornament band"/>
      <circle class="mark-dot" cx="62" cy="22" r="11"/>
      <text class="script brand-name" x="78" y="28" font-size="17">Velarisse</text>
      <text class="script word-sensual" x="60" y="62" font-size="16">Sensual</text>
      <text class="script" x="95" y="82" font-size="23" text-anchor="middle"><tspan class="word-massage">Massage</tspan><tspan class="word-cream">Cream</tspan></text>
      <path class="rose-wave" d="M0,97 Q95,88 190,103 L190,112 L0,112 Z"/>
    </g>
    <!-- brand end panel, reused upside down for the bottom panel -->
    <g id="brand-face">
      <rect class="damask-band" x="0" y="45" width="190" height="62" role="img" aria-label="Soft silver damask ornament band"/>
      <circle class="mark-dot" cx="95" cy="76" r="28"/>
      <text class="script brand-name" x="95" y="146" font-size="30" text-anchor="middle">Velarisse</text>
      <text class="script tagline" x="95" y="172" font-size="16" text-anchor="middle">Glow from the Core</text>
      <path class="rose-wave" d="M0,192 Q95,176 190,196 L190,218 L0,218 Z"/>
    </g>
  </defs>

  <!-- flat jar label -->
  <g class="jar-label" transform="translate(285,120) scale(2)">
    <use href="#product-face"/>
  </g>

  <!-- carton dieline -->
  <g class="carton">
    <g class="dieline">
      <path d="M457,573 L457,362 Q457,340 479,340 L625,340 Q647,340 647,362 L647,573"/>
      <path d="M457,685 L457,913 Q457,935 479,935 L625,935 Q647,935 647,913 L647,685"/>
      <path d="M72,575 L42,583 L42,677 L72,685"/>
      <path d="M265,573 L265,482 L290,458 L457,458"/>
      <path d="M647,458 L812,458 L838,482 L838,573"/>
      <path d="M265,685 L265,778 L290,803 L457,803"/>
      <path d="M647,803 L812,803 L838,778 L838,685"/>
      <rect x="72" y="573" width="766" height="112"/>
      <line x1="265" y1="573" x2="265" y2="685"/>
      <line x1="457" y1="573" x2="457" y2="685"/>
      <line x1="647" y1="573" x2="647" y2="685"/>
    </g>
    <line class="crease" x1="457" y1="356" x2="647" y2="356"/>
    <line class="crease" x1="457" y1="919" x2="647" y2="919"/>

    <g class="panel-brand-top" transform="translate(457,355)"><use href="#brand-face"/></g>
    <g class="panel-brand-bottom" transform="translate(647,903) rotate(180)"><use href="#brand-face"/></g>

    <g class="panel-side" transform="translate(75,573)"><use href="#product-face"/></g>
    <g class="panel-front" transform="translate(265,573)"><use href="#product-face"/></g>
    <g class="panel-side" transform="translate(457,573)"><use href="#product-face"/></g>
    <g class="panel-back" transform="translate(647,573)"><use href="#product-face"/></g>
  </g>
</svg>
</body>
</html>
```